Newspaper ad advertising bathroom adaptations for the less-abled and disabled.

This ad is to really promote bathroom adaptations that are suited to the clients needs, so more care led rather than design led. Important for the ad to be easy to read and easy to understand. Clearly states bathroom conversions from £4,999 to help qualify leads generated from the ad. We are looking to reach out to anyone whose bathroom is becoming more challenging because of mobility issues so we can use our excellent industry knowledge and personal family experience to come up with solutions that really work for the client

Target Market(s)

predominately older people

Industry/Entity Type

Health And Wellness

Font styles to use
Serif

Colors

Designer to choose colors to be used in the design.

Requirements
Must have
• It must have the content that is included in advert i have attached. Use where possible the photos of the actual jobs we've done to make it relatable for the client to see real jobs.
Nice to have
• some added pictures of mobility bathroom equipment including walk-in baths, walk-in showers and wetroom flooring.
Should not have
• anything too heavy on the eye.

```html
<!DOCTYPE html>
<html lang="en">
<head>
<meta charset="utf-8">
<title>Harbour Adaptations – Bathroom Adaptations Ad</title>
<link href="https://fonts.googleapis.com/css2?family=Open+Sans:wght@400;600&family=Arimo:ital,wght@0,400;0,700;1,400;1,700&display=swap" rel="stylesheet">
<style>
  :root {
    --page-bg: #555555;
    --teal: #16a29f;
    --teal-deep: #0c8c89;
    --navy: #0f3c77;
    --white: #ffffff;
    --orange: #e8732c;
    --logo-navy: #1d3a6e;
  }
  * { margin: 0; padding: 0; box-sizing: border-box; }
  html, body { width: 1200px; height: 1200px; overflow: hidden; background: var(--page-bg); }
  .flyer-stage { position: relative; width: 1200px; height: 1200px; }
  .flyer {
    position: absolute; left: 193px; top: 30px;
    width: 897px; height: 1258px;
    transform: scale(0.906); transform-origin: 0 0;
    background: linear-gradient(160deg, var(--teal-deep) 0%, var(--teal) 45%, var(--teal-deep) 100%);
    overflow: hidden; color: var(--white);
    font-family: "Arimo", Arial, sans-serif;
  }
  .photo-panels { position: absolute; inset: 0; }
  .brand-box {
    position: absolute; left: 88px; top: 55px; width: 277px; height: 73px;
    background: var(--white); border: 3px solid var(--orange); border-radius: 9px;
    display: flex; align-items: center; gap: 12px; padding-left: 18px;
  }
  .brand-box__dot { width: 40px; height: 40px; border-radius: 50%; background: var(--logo-navy); flex: none; }
  .brand-box__name { font-family: "Arimo", Arial, sans-serif; font-weight: 700; font-size: 22px; color: var(--logo-navy); line-height: 1.1; }
  .headline {
    position: absolute; left: 25px; top: 150px; width: 560px;
    font-style: italic; font-weight: 400; font-size: 43px; line-height: 46px;
  }
  .headline__solution { display: block; font-size: 47px; margin-top: 3px; }
  .subhead {
    position: absolute; left: 27px; top: 320px;
    font-weight: 700; font-size: 38px; line-height: 42px;
  }
  .price-band {
    position: absolute; left: 0; top: 463px; width: 497px; height: 125px;
    background: var(--navy); border-radius: 0 32px 32px 0;
    padding: 6px 0 0 32px;
    font-weight: 700; font-style: italic; font-size: 28px; line-height: 36px;
  }
  .price-band__from { font-size: 25px; }
  .price-band__amount { font-size: 34px; }
  .care-line {
    position: absolute; left: 31px; top: 594px; width: 560px;
    font-family: "Open Sans", Arial, sans-serif; font-weight: 600; font-size: 25px; line-height: 27px;
  }
  .feature-list {
    position: absolute; left: 42px; top: 658px; list-style: none;
    font-family: "Open Sans", Arial, sans-serif; font-size: 17px; line-height: 26.4px;
  }
  .feature-list li { display: flex; gap: 8px; align-items: flex-start; }
  .feature-list svg { width: 14px; height: 14px; margin-top: 6px; flex: none; }
  .feature-list__multi { line-height: 21px; margin-top: 3px; }
  .accreditations {
    position: absolute; left: 68px; top: 1089px; width: 211px; height: 52px;
    background: var(--white); display: flex; align-items: center; justify-content: space-around; padding: 0 10px;
  }
  .accreditations span { display: block; background: #d9dde2; }
  .badge-rect { width: 40px; height: 28px; }
  .badge-circle { width: 32px; height: 32px; border-radius: 50%; }
  .badge-wide { width: 54px; height: 20px; }
  .footer-band { position: absolute; left: 0; top: 1155px; width: 897px; height: 103px; background: var(--navy); }
  .footer-cta {
    position: absolute; left: 34px; top: 1166px;
    font-weight: 700; font-size: 21px; line-height: 24px; text-transform: uppercase;
  }
  .footer-contact { position: absolute; left: 33px; top: 1221px; font-size: 14px; }
</style>
</head>
<body>
<div class="flyer-stage">
  <div class="flyer">
    <div class="footer-band"></div>

    <svg class="photo-panels" viewBox="0 0 897 1258" width="897" height="1258">
      <defs>
        <linearGradient id="tileTone" x1="0" y1="0" x2="1" y2="1">
          <stop offset="0" stop-color="#cfd8d4"/><stop offset="1" stop-color="#8fa8a0"/>
        </linearGradient>
        <linearGradient id="whiteTone" x1="0" y1="0" x2="1" y2="1">
          <stop offset="0" stop-color="#eef0ef"/><stop offset="1" stop-color="#b9c7c2"/>
        </linearGradient>
      </defs>
      <polygon points="897,350 897,440 855,395" fill="#0f3c77"/>
      <polygon points="897,710 897,790 857,750" fill="#0f3c77"/>
      <g stroke="#ffffff" stroke-width="6">
        <polygon role="img" aria-label="Photo of a walk-in shower with a shower seat" fill="url(#whiteTone)" points="843,23 903,83 903,300 843,360 675,192"/>
        <polygon role="img" aria-label="Photo of a glass shower enclosure beside a wall-hung basin" fill="url(#tileTone)" points="660,213 830,382 660,550 490,383"/>
        <polygon role="img" aria-label="Photo of a raised toilet in a tiled bathroom" fill="url(#tileTone)" points="842,395 903,456 903,670 842,730 674,562"/>
        <polygon role="img" aria-label="Photo of a shower rail and thermostatic valve" fill="url(#whiteTone)" points="667,582 835,750 667,920 497,753"/>
        <polygon role="img" aria-label="Photo of a countertop basin on a white vanity" fill="url(#tileTone)" points="837,790 903,856 903,1270 650,1270 510,1125"/>
      </g>
    </svg>

    <div class="brand-box">
      <span class="brand-box__dot"></span>
      <span class="brand-box__name">Harbour<br>Adaptations</span>
    </div>

    <h1 class="headline">Is your bathroom becoming more challenging?<span class="headline__solution">We have the solution...</span></h1>

    <h2 class="subhead">Bathroom adaptations<br>for the elderly, disabled<br>and less abled</h2>

    <div class="price-band">
      Adapted bathroom conversions<br>to help with your mobility needs<br>
      <span class="price-band__from">from</span> <span class="price-band__amount">£4,999*</span>
    </div>

    <p class="care-line">We care passionately about installing a quality bathroom that really works for your needs</p>

    <ul class="feature-list">
      <li><svg viewBox="0 0 14 14"><rect x="1" y="3" width="10" height="10" fill="none" stroke="#fff" stroke-width="1.3"/><path d="M3 7l3 3 7-8" fill="none" stroke="#fff" stroke-width="1.8"/></svg>Existing bathroom to wetroom conversions</li>
      <li><svg viewBox="0 0 14 14"><rect x="1" y="3" width="10" height="10" fill="none" stroke="#fff" stroke-width="1.3"/><path d="M3 7l3 3 7-8" fill="none" stroke="#fff" stroke-width="1.8"/></svg>Walk-in showers &amp; wetrooms tailored to meet your needs</li>
      <li><svg viewBox="0 0 14 14"><rect x="1" y="3" width="10" height="10" fill="none" stroke="#fff" stroke-width="1.3"/><path d="M3 7l3 3 7-8" fill="none" stroke="#fff" stroke-width="1.8"/></svg>Full bathroom mobility enablement</li>
      <li><svg viewBox="0 0 14 14"><rect x="1" y="3" width="10" height="10" fill="none" stroke="#fff" stroke-width="1.3"/><path d="M3 7l3 3 7-8" fill="none" stroke="#fff" stroke-width="1.8"/></svg>Free no obligation home assessment</li>
      <li><svg viewBox="0 0 14 14"><rect x="1" y="3" width="10" height="10" fill="none" stroke="#fff" stroke-width="1.3"/><path d="M3 7l3 3 7-8" fill="none" stroke="#fff" stroke-width="1.8"/></svg>Full detailed pre-install survey</li>
      <li><svg viewBox="0 0 14 14"><rect x="1" y="3" width="10" height="10" fill="none" stroke="#fff" stroke-width="1.3"/><path d="M3 7l3 3 7-8" fill="none" stroke="#fff" stroke-width="1.8"/></svg>Fully project managed dedicated installation team</li>
      <li><svg viewBox="0 0 14 14"><rect x="1" y="3" width="10" height="10" fill="none" stroke="#fff" stroke-width="1.3"/><path d="M3 7l3 3 7-8" fill="none" stroke="#fff" stroke-width="1.8"/></svg>Full insurance backed guarantee on all adaptations</li>
      <li><svg viewBox="0 0 14 14"><rect x="1" y="3" width="10" height="10" fill="none" stroke="#fff" stroke-width="1.3"/><path d="M3 7l3 3 7-8" fill="none" stroke="#fff" stroke-width="1.8"/></svg>All tiling, electrics, plumbing etc carried out</li>
      <li><svg viewBox="0 0 14 14"><rect x="1" y="3" width="10" height="10" fill="none" stroke="#fff" stroke-width="1.3"/><path d="M3 7l3 3 7-8" fill="none" stroke="#fff" stroke-width="1.8"/></svg>Bathing enabling equipment</li>
      <li><svg viewBox="0 0 14 14"><rect x="1" y="3" width="10" height="10" fill="none" stroke="#fff" stroke-width="1.3"/><path d="M3 7l3 3 7-8" fill="none" stroke="#fff" stroke-width="1.8"/></svg>Work closely with occupational therapists</li>
      <li><svg viewBox="0 0 14 14"><rect x="1" y="3" width="10" height="10" fill="none" stroke="#fff" stroke-width="1.3"/><path d="M3 7l3 3 7-8" fill="none" stroke="#fff" stroke-width="1.8"/></svg>Anti-slip safety flooring</li>
      <li><svg viewBox="0 0 14 14"><rect x="1" y="3" width="10" height="10" fill="none" stroke="#fff" stroke-width="1.3"/><path d="M3 7l3 3 7-8" fill="none" stroke="#fff" stroke-width="1.8"/></svg>Maintenance free shower panelling</li>
      <li><svg viewBox="0 0 14 14"><rect x="1" y="3" width="10" height="10" fill="none" stroke="#fff" stroke-width="1.3"/><path d="M3 7l3 3 7-8" fill="none" stroke="#fff" stroke-width="1.8"/></svg>Walk-in easy access baths</li>
      <li><svg viewBox="0 0 14 14"><rect x="1" y="3" width="10" height="10" fill="none" stroke="#fff" stroke-width="1.3"/><path d="M3 7l3 3 7-8" fill="none" stroke="#fff" stroke-width="1.8"/></svg>Specialist wash &amp; dry toilets</li>
      <li class="feature-list__multi"><svg viewBox="0 0 14 14"><rect x="1" y="3" width="10" height="10" fill="none" stroke="#fff" stroke-width="1.3"/><path d="M3 7l3 3 7-8" fill="none" stroke="#fff" stroke-width="1.8"/></svg><span>Fully accredited to HomeCheck, MATA and<br>the Fair Trade Homes Association</span></li>
    </ul>

    <div class="accreditations" aria-label="Accreditation badges">
      <span class="badge-rect"></span>
      <span class="badge-circle"></span>
      <span class="badge-rect"></span>
      <span class="badge-wide"></span>
    </div>

    <p class="footer-cta">Call today for a no obligation home<br>assessment or a brochure</p>
    <p class="footer-contact">01632 960 411 &nbsp;|&nbsp; hello@harbouradaptations.com &nbsp;|&nbsp; www.harbouradaptations.com</p>
  </div>
</div>
</body>
</html>
```